Price list for young Relaxon clinic

I require a price list/Treatment menu for clinic

To include:
Logo
Address
Phone number
Website

List of services and Prices
Relaxon 1 area £100
Relaxon 2 areas £150
Relaxon 3 areas £200
Lip Enhancement 0.5ml £100
Lip Enhancement 1ml £200
Facial Fillers £200 per 1ml
Volumiq £450 per session (2 vials - must be bought as a course)
Non Surgical Face Lift (Thread Lift) £600 per area
Skin Press Full Face £250
Skin Press Small Per Small Area £100
Cryo Therapy £60
Chemical Peel Light Peel and Microdermabrasion £85
Chemical Peel Deep Peel £150
Consultation £30 redeemable against service
Relaxon Top Up Relaxon £50 (must be within 2 weeks of 1st treatment)
Filler Top Up £100 (must be within 2 weeks of 1st appointment)

Open Hours
Updates

Company Name: HVM Address: 482 Pellbrook Road, 6 Warnford High Street, KT4 3JQ Phone: 0208 947 2186 Website: www.hollyvanmereaesthetics.co.uk

Please add more colour

Needs to be much cleaner and simpler Front page to include logo and price list Back page to inculde open hours and contact information including google map. Please no images with needles. Images of lips and faces are good, but try not to crowd copy on the pagei. No copy on top of images. White, grey, black and reds are good on colouring.

Target Market(s)

young market ages 22-45 years old mainly female
modern

Industry/Entity Type

Clinic

Number of Pages Required

4 page

Requirements
Must have
• Logo - logo must be in colour grey/silver
• Address (small map?)
• Phone number
• Web address
• Services
• Open hours
• Prices
• Images

```html
<!DOCTYPE html>
<html lang="en">
<head>
<meta charset="utf-8">
<title>HVM Price List</title>
<link rel="stylesheet" href="https://fonts.googleapis.com/css2?family=Crimson+Text:wght@400;600&family=PT+Sans:wght@400&display=swap">
<style>
  :root {
    --paper: #ffffff;
    --brand-grey: #9a9a9a;
    --ink: #4a4a4a;
    --ink-dark: #222222;
    --rule-red: #e0595a;
    --text-red: #d8383a;
    --coral: #ef8073;
    --mask-tone: #f6cf9c;
  }
  * { margin: 0; padding: 0; box-sizing: border-box; }
  html, body { width: 1200px; height: 848px; overflow: hidden; background: var(--paper); }
  .sheet { position: relative; width: 1200px; height: 848px; background: var(--paper); overflow: hidden; }

  .swoosh { position: absolute; left: 0; top: 0; z-index: 0; }

  .brand { position: absolute; left: 164px; top: 48px; width: 240px; text-align: center; z-index: 1; }
  .brand-disc { width: 96px; height: 96px; border-radius: 50%; background: var(--brand-grey); margin: 0 auto 10px; }
  .brand-name {
    font-family: "Crimson Text", serif; font-weight: 400; color: var(--brand-grey);
    text-transform: uppercase; white-space: nowrap;
  }
  .brand-name .line-top { display: block; font-size: 16px; letter-spacing: 3px; line-height: 18px; }
  .brand-name .line-bottom { display: block; font-size: 24px; letter-spacing: 3px; line-height: 24px; }

  .contact {
    position: absolute; right: 177px; top: 82px; text-align: right; z-index: 1;
    font-family: "Crimson Text", serif; font-size: 23px; line-height: 26px; color: var(--ink);
  }
  .contact .label { text-decoration: underline; }

  .price-table {
    position: absolute; left: 175px; top: 209px; width: 848px; z-index: 1;
    border-collapse: collapse;
  }
  .price-table th, .price-table td {
    border: 1.5px solid var(--rule-red); height: 30px; padding: 0 0 0 16px;
    text-align: left; vertical-align: middle; color: var(--text-red); white-space: nowrap;
  }
  .price-table th { font-family: "Crimson Text", serif; font-weight: 600; font-size: 21px; }
  .price-table td { font-family: "PT Sans", sans-serif; font-size: 20.5px; }
  .price-table .col-price { width: 174px; padding-left: 52px; }

  .masks-art {
    position: absolute; left: 993px; top: 667px; width: 148px; height: 143px; z-index: 2;
    border-radius: 30px 40px 50px 40px;
    background: linear-gradient(135deg, var(--mask-tone), #f0b98a);
  }

  .website {
    position: absolute; left: 621px; top: 797px; z-index: 1;
    font-family: "Crimson Text", serif; font-size: 21px; color: var(--ink-dark);
  }
</style>
</head>
<body>
<div class="sheet">
  <svg class="swoosh" width="1200" height="848" viewBox="0 0 1200 848" aria-hidden="true">
    <path d="M0,704 C40,692 90,684 150,684" fill="none" stroke="var(--coral)" stroke-width="4"/>
    <path d="M0,770 C60,742 130,728 200,732 C330,742 480,800 600,848 L520,848 C430,806 320,772 220,764 C140,758 70,786 0,818 Z" fill="var(--coral)"/>
  </svg>

  <div class="brand">
    <div class="brand-disc"></div>
    <div class="brand-name"><span class="line-top">Holly Vanmere</span><span class="line-bottom">Aesthetics</span></div>
  </div>

  <div class="contact">
    <div><span class="label">HVM Address:</span></div>
    <div>482 Pellbrook Road, 6 Warnford</div>
    <div>High Street, KT4 3JQ</div>
    <div><span class="label">Phone:</span> 0208 947 2186</div>
  </div>

  <table class="price-table">
    <thead>
      <tr><th>Services</th><th class="col-price">Price</th></tr>
    </thead>
    <tbody>
      <tr><td>Relaxon 1 area</td><td class="col-price">£100</td></tr>
      <tr><td>Relaxon 2 areas</td><td class="col-price">£150</td></tr>
      <tr><td>Relaxon 3 areas</td><td class="col-price">£200</td></tr>
      <tr><td>Lip Enhancement 0.5ml</td><td class="col-price">£100</td></tr>
      <tr><td>Lip Enhancement 1ml</td><td class="col-price">£200</td></tr>
      <tr><td>Facial Fillers (per 1ml)</td><td class="col-price">£200</td></tr>
      <tr><td>Volumiq (per session) (2 vials - must be bought as a course)</td><td class="col-price">£450</td></tr>
      <tr><td>Non Surgical Face Lift (Thread Lift) (per area)</td><td class="col-price">£600</td></tr>
      <tr><td>Skin Press Full Face</td><td class="col-price">£250</td></tr>
      <tr><td>Skin Press Small (Per Small Area)</td><td class="col-price">£100</td></tr>
      <tr><td>Cryo Therapy</td><td class="col-price">£60</td></tr>
      <tr><td>Chemical Peel Light Peel and Microdermabrasion</td><td class="col-price">£85</td></tr>
      <tr><td>Chemical Peel Deep Peel</td><td class="col-price">£150</td></tr>
      <tr><td>Consultation redeemable against service</td><td class="col-price">£30</td></tr>
      <tr><td>Relaxon Top Up Relaxon (must be within 2 weeks of 1st treatment)</td><td class="col-price">£50</td></tr>
      <tr><td>Filler Top Up (must be within 2 weeks of 1st appointment)</td><td class="col-price">£100</td></tr>
    </tbody>
  </table>

  <div class="masks-art" role="img" aria-label="Illustration of two theatre masks, comedy and tragedy, in warm peach tones"></div>

  <div class="website">www.hollyvanmereaesthetics.co.uk</div>
</div>
</body>
</html>
```